Will you marry me post card

I am just looking for a postcard to send my partner that will ask him to marry me.
I plan on creating about 200 of them and mailing them all at once so that he gets them all on the same day.
They should all be similar or could have a few different options.
I would like it simple, elegant, clean and crisp. No images, just text or icons

My only requirement is the text, "will you marry me?" in all lowercase -- any fonts, can be big, small, varying sizes, repeated, whole card, tiny space, don't care...just amazing design. BUT SIMPLE!

```html
<!DOCTYPE html>
<html lang="en">
<head>
<meta charset="UTF-8">
<title>will you marry me? — postcard</title>
<link rel="stylesheet" href="https://fonts.googleapis.com/css2?family=Great+Vibes&display=swap">
<style>
  :root {
    --backdrop: #e9e6e2;
    --card-white: #ffffff;
    --ink-light: #ffffff;
    --grid-line: rgba(255, 255, 255, 0.06);
    --glow-yellow: #ffe45a;
    --glow-amber: #f4b23c;
    --olive: #8ea12e;
    --leaf-green: #3f8a3a;
    --deep-teal: #143a3c;
    --plum: #4a2a3a;
    --wine: #4a1414;
    --rust: #7a3a18;
  }
  * { margin: 0; padding: 0; box-sizing: border-box; }
  html, body {
    width: 1200px;
    height: 548px;
    overflow: hidden;
    background: var(--backdrop);
  }
  .postcard {
    position: absolute;
    left: 75px;
    top: 72px;
    width: 1049px;
    height: 403px;
    display: flex;
    box-shadow: 0 6px 18px rgba(0, 0, 0, 0.25);
  }
  .postcard-front {
    position: relative;
    width: 524px;
    height: 100%;
    overflow: hidden;
    background:
      radial-gradient(ellipse 220px 170px at 62% 8%, var(--glow-yellow) 0%, rgba(255, 228, 90, 0) 100%),
      radial-gradient(ellipse 260px 240px at 52% 30%, var(--glow-amber) 0%, rgba(244, 178, 60, 0) 100%),
      radial-gradient(ellipse 240px 260px at 0% 0%, var(--olive) 0%, rgba(142, 161, 46, 0) 100%),
      radial-gradient(ellipse 240px 280px at 100% 35%, var(--leaf-green) 0%, rgba(63, 138, 58, 0) 100%),
      radial-gradient(ellipse 260px 240px at 100% 100%, var(--deep-teal) 0%, rgba(20, 58, 60, 0) 100%),
      radial-gradient(ellipse 180px 160px at 68% 100%, var(--plum) 0%, rgba(74, 42, 58, 0) 100%),
      radial-gradient(ellipse 260px 230px at 0% 100%, var(--wine) 0%, rgba(74, 20, 20, 0) 100%),
      linear-gradient(160deg, var(--olive) 0%, var(--glow-amber) 35%, var(--rust) 65%, var(--deep-teal) 100%);
  }
  .grid-texture {
    position: absolute;
    inset: 0;
    background:
      repeating-linear-gradient(0deg, var(--grid-line) 0 1px, transparent 1px 19px),
      repeating-linear-gradient(90deg, var(--grid-line) 0 1px, transparent 1px 19px);
  }
  .postcard-back {
    width: 525px;
    height: 100%;
    background: var(--card-white);
  }
  .hearts {
    position: absolute;
    inset: 0;
    width: 100%;
    height: 100%;
  }
  .hearts use { fill: var(--ink-light); }
  .proposal {
    position: absolute;
    left: 0;
    top: 0;
    width: 100%;
    height: 100%;
    font-family: 'Great Vibes', cursive;
    color: var(--ink-light);
    font-weight: 400;
    line-height: 1;
  }
  .proposal span {
    position: absolute;
    white-space: nowrap;
  }
  .proposal .line-will  { left: 155px; top: 78px;  font-size: 118px; }
  .proposal .line-you   { left: 290px; top: 118px; font-size: 100px; }
  .proposal .line-marry { left: 118px; top: 186px; font-size: 136px; }
  .proposal .line-me    { left: 200px; top: 285px; font-size: 100px; }
</style>
</head>
<body>
  <main class="postcard">
    <section class="postcard-front">
      <div class="grid-texture" aria-hidden="true"></div>
      <svg class="hearts" viewBox="0 0 524 403" aria-hidden="true">
        <defs>
          <symbol id="heart" viewBox="0 0 20 18">
            <path d="M10 17.5 C4 12.5 0 9.5 0 5.3 0 2.3 2.3 0 5.2 0 7.3 0 9 1.2 10 3 11 1.2 12.7 0 14.8 0 17.7 0 20 2.3 20 5.3 20 9.5 16 12.5 10 17.5Z"/>
          </symbol>
        </defs>
        <use href="#heart" x="84" y="54" width="22" height="20"/>
        <use href="#heart" x="117" y="16" width="8" height="7"/>
        <use href="#heart" x="52" y="71" width="9" height="8"/>
        <use href="#heart" x="216" y="88" width="20" height="18"/>
        <use href="#heart" x="319" y="81" width="9" height="8"/>
        <use href="#heart" x="422" y="54" width="24" height="22"/>
        <use href="#heart" x="492" y="37" width="9" height="8"/>
        <use href="#heart" x="472" y="128" width="9" height="8"/>
        <use href="#heart" x="38" y="167" width="11" height="10"/>
        <use href="#heart" x="120" y="170" width="9" height="8"/>
        <use href="#heart" x="352" y="209" width="16" height="14"/>
        <use href="#heart" x="467" y="234" width="22" height="20"/>
        <use href="#heart" x="68" y="356" width="16" height="14"/>
        <use href="#heart" x="434" y="348" width="9" height="8"/>
        <use href="#heart" x="268" y="391" width="9" height="8"/>
      </svg>
      <h1 class="proposal" aria-label="will you marry me?">
        <span class="line-will">will</span>
        <span class="line-you">you</span>
        <span class="line-marry">marry</span>
        <span class="line-me">me?</span>
      </h1>
    </section>
    <section class="postcard-back"></section>
  </main>
</body>
</html>
```